Plate Parade! Digital Order Web App

This is a web app on mobile phone, for consumers to order food inside a restaurant using their phones. we have done up the flow but we need to revamp UI design. pls have a look at our current web on your mobile phone:
https://demo.pesanly.app/o/KWLM/274615

CURRENT DESIGN.
1. food category on left side, always shown. menu items in list view with image.
2. when we click on an item, there is popup page, to select modifiers, or quantity.
3. order review page(cart page) is quite messy now, need a complete new look.
4 payment page(no need to design, handle by Paxtel)
5. order confirmation page. success or error return

DESIGN requirements:
please browse through and click to order with current page above. we have put in lots of thoughts and effort for current flow, the new design should base on this flow.
1. web app. no zoom in/out is allowed for users. responsive html to suit different mobile phone screen size. modern fonts.
2. PAGES needed:
home/welcome page,
well laid out menu items page,
single item page, with add on choice and modifier
cart page(to include recommended items, ordered item list, remove item total, changeable quantity,
confirmation page(success, fail)

DELIVERABLES - responsive html, fonts, images asset such as icons, animation, button images(suitable for commercial use without further third party loyalty fee)

Hi all if we have left a comment on ur design, please revise accordingly and we will conclude it soon!

Target Market(s)

young diners who order food on their mobile phone.

Industry/Entity Type

Restaurant

Coding

Coded - Design and coding required

Number of Pages Required

5+ page

Colors

Designer to choose colors to be used in the design.

Requirements
Must have
• - lively, appetising colors while making the page easy to read. easy on eyes.
• - consistency. fonts used.
Nice to have
• - 2 color schemes
• - html codes. we will top up if you can deliver coded html.
Should not have
• - should not have more than 3 colors
• - should not have more than 3 different fonts
• - should not use colors that are dull

```html
<!DOCTYPE html>
<html lang="en">
<head>
<meta charset="utf-8">
<meta name="viewport" content="width=1200, user-scalable=no">
<title>Tabletop – Order Confirmed</title>
<link href="https://fonts.googleapis.com/css2?family=Raleway:wght@400;500;600;700&display=swap" rel="stylesheet">
<style>
  :root {
    --header-top: #86aaf3;
    --header-bottom: #7aa1f7;
    --page-bg: #fafafa;
    --card-bg: #ffffff;
    --ink: #2b2b2b;
    --muted: #777777;
    --price: #8a8a8a;
    --accent: #f5435a;
    --star: #ee8a2a;
    --rule: #ececec;
    --footer-bg: #3a3a3d;
    --footer-ink: #ffffff;
  }
  * { box-sizing: border-box; margin: 0; padding: 0; }
  html, body { width: 1200px; height: 2499px; overflow: hidden; }
  body {
    position: relative;
    font-family: "Raleway", sans-serif;
    color: var(--ink);
    background: linear-gradient(180deg, var(--header-top), var(--header-bottom));
  }
  .app-header {
    position: absolute; left: 0; top: 0; width: 1200px; height: 180px;
  }
  .menu-toggle { position: absolute; left: 60px; top: 69px; }
  .brand {
    position: absolute; left: 0; right: 0; top: 52px;
    text-align: center; color: #fff; font-weight: 700; font-size: 56px;
  }
  .cart-button { position: absolute; left: 1052px; top: 60px; }
  .cart-badge {
    position: absolute; left: 1099px; top: 66px; width: 40px; height: 40px;
    border-radius: 50%; background: var(--accent); color: #fff;
    font-size: 22px; font-weight: 700; text-align: center; line-height: 40px;
  }
  .page-body {
    position: absolute; left: 0; top: 174px; width: 1200px; height: 2226px;
    background: var(--page-bg); border-radius: 120px 120px 0 0;
  }
  .card {
    position: absolute; left: 81px; width: 1038px;
    background: var(--card-bg); border-radius: 66px;
    box-shadow: 0 9px 36px rgba(0,0,0,0.08);
  }
  .confirmation { top: 267px; height: 1176px; text-align: center; }
  .success-mark { position: absolute; left: 402px; top: 162px; }
  .confirm-title { position: absolute; left: 0; right: 0; top: 463px; font-size: 54px; font-weight: 700; }
  .order-number { position: absolute; left: 0; right: 0; top: 602px; font-size: 47px; font-weight: 500; }
  .confirm-note {
    position: absolute; left: 0; right: 0; top: 694px;
    font-size: 38px; line-height: 60px; color: var(--muted);
  }
  .points { position: absolute; left: 0; right: 0; font-size: 50px; font-weight: 600; }
  .points strong { font-weight: 700; }
  .points svg { vertical-align: -4px; margin-left: 28px; }
  .points-earned { top: 1140px; }
  .points-total { top: 1236px; }
  .confirmation .points-earned { top: 873px; }
  .confirmation .points-total { top: 969px; }

  .summary { top: 1536px; height: 750px; }
  .summary-title { position: absolute; left: 93px; top: 96px; font-size: 51px; font-weight: 700; }
  .summary-rule { position: absolute; left: 93px; top: 181px; width: 855px; height: 6px; background: var(--rule); border-radius: 3px; }
  .line-item { position: absolute; left: 93px; width: 855px; height: 168px; }
  .line-item:nth-of-type(1) { top: 255px; }
  .line-item:nth-of-type(2) { top: 489px; }
  .item-photo {
    position: absolute; left: 0; top: 0; width: 174px; height: 168px;
    border-radius: 30px; box-shadow: 0 9px 18px rgba(0,0,0,0.18);
  }
  .photo-beans { background: linear-gradient(135deg, #6b4a2e, #5f8a3a 55%, #4b6d2a); }
  .photo-chips { background: linear-gradient(135deg, #7a2e22, #b2533d 55%, #8f3c2c); }
  .item-qty { position: absolute; left: 225px; top: 60px; font-size: 38px; font-weight: 500; }
  .item-name { position: absolute; left: 330px; top: 58px; font-size: 40px; font-weight: 500; }
  .item-price { position: absolute; right: 0; top: 60px; font-size: 38px; font-weight: 600; color: var(--price); }

  .app-footer {
    position: absolute; left: 0; top: 2400px; width: 1200px; height: 99px;
    background: var(--footer-bg); color: var(--footer-ink);
    font-size: 21px; font-weight: 600;
  }
  .copyright { position: absolute; left: 96px; top: 38px; }
  .footer-links { position: absolute; right: 93px; top: 38px; }
  .footer-links span + span { margin-left: 36px; }
</style>
</head>
<body>
  <header class="app-header">
    <svg class="menu-toggle" width="60" height="42" viewBox="0 0 60 42" aria-label="Menu">
      <g stroke="#fff" stroke-width="6" stroke-linecap="round">
        <line x1="3" y1="3" x2="57" y2="3"/><line x1="3" y1="21" x2="57" y2="21"/><line x1="3" y1="39" x2="57" y2="39"/>
      </g>
    </svg>
    <div class="brand">Tabletop</div>
    <svg class="cart-button" width="66" height="66" viewBox="0 0 66 66" aria-label="Cart">
      <g fill="none" stroke="#fff" stroke-width="5" stroke-linejoin="round" stroke-linecap="round">
        <path d="M3 8 h10 l8 34 h34 l6 -24 h-42"/>
      </g>
      <circle cx="25" cy="54" r="5" fill="#fff"/><circle cx="50" cy="54" r="5" fill="#fff"/>
    </svg>
    <div class="cart-badge">2</div>
  </header>

  <main class="page-body"></main>

  <section class="card confirmation">
    <svg class="success-mark" width="234" height="234" viewBox="0 0 234 234" aria-label="Success">
      <circle cx="117" cy="117" r="117" fill="var(--accent)"/>
      <path d="M62 120 l36 36 l74 -76" fill="none" stroke="#fff" stroke-width="20" stroke-linecap="round" stroke-linejoin="round"/>
    </svg>
    <h1 class="confirm-title">Order Confirmed !</h1>
    <p class="order-number">Your Order no is : 1497</p>
    <p class="confirm-note">Please proceed to the collection<br>point for your order</p>
    <p class="points points-earned">Earned : <strong>1560.22</strong>
      <svg width="48" height="46" viewBox="0 0 24 23"><path fill="var(--star)" d="M12 0l3.7 7.5 8.3 1.2-6 5.8 1.4 8.3L12 18.9 4.6 22.8 6 14.5 0 8.7l8.3-1.2z"/></svg>
    </p>
    <p class="points points-total">Total : <strong>5920.22</strong>
      <svg width="48" height="46" viewBox="0 0 24 23"><path fill="var(--star)" d="M12 0l3.7 7.5 8.3 1.2-6 5.8 1.4 8.3L12 18.9 4.6 22.8 6 14.5 0 8.7l8.3-1.2z"/></svg>
    </p>
  </section>

  <section class="card summary">
    <h2 class="summary-title">Summary</h2>
    <div class="summary-rule"></div>
    <div>
      <div class="line-item">
        <div class="item-photo photo-beans" role="img" aria-label="Photo of grilled string bean skewers"></div>
        <span class="item-qty">4 x</span>
        <span class="item-name">Grilled String Bean</span>
        <span class="item-price">S$ 2.80</span>
      </div>
      <div class="line-item">
        <div class="item-photo photo-chips" role="img" aria-label="Photo of grilled potato chip skewers"></div>
        <span class="item-qty">2 x</span>
        <span class="item-name">Grilled Potato Chip</span>
        <span class="item-price">S$ 2.80</span>
      </div>
    </div>
  </section>

  <footer class="app-footer">
    <span class="copyright">copyright2019tabletop</span>
    <span class="footer-links"><span>Terms &amp; Conditions</span><span>Privacy Policy</span></span>
  </footer>
</body>
</html>
```